Redesign of Business Cards to Update them!

We want a full overhaul of our business cards! We have a design that is almost 5 years old and it needs to be updated to be current

Address is 437 Dunmore Lane Suite C San Bernardino CA 92408
PH: 9094718263
Zorlivo.com

Hours M-F 10AM-4PM
Sat and Sunday Closed

```html
<!DOCTYPE html>
<html lang="en">
<head>
<meta charset="utf-8">
<title>Zorlivo Business Card</title>
<link href="https://fonts.googleapis.com/css2?family=Roboto:wght@400;500;700;900&display=swap" rel="stylesheet">
<style>
  :root {
    --brand-red: #fb0000;
    --ink-black: #0a0a0a;
    --paper-white: #ffffff;
    --card-white: #f4f5f7;
    --backdrop: #e6e3de;
  }
  * { margin: 0; padding: 0; box-sizing: border-box; }
  html, body {
    width: 1200px;
    height: 800px;
    overflow: hidden;
    background: var(--backdrop);
    font-family: 'Roboto', Arial, sans-serif;
  }
  .canvas {
    position: relative;
    width: 1200px;
    height: 800px;
    display: flex;
    align-items: center;
    justify-content: center;
    gap: 40px;
  }
  .card {
    width: 540px;
    height: 309px;
    border-radius: 4px;
    box-shadow: 0 10px 28px rgba(0,0,0,0.18);
    position: relative;
    overflow: hidden;
  }
  .card-front {
    background: var(--brand-red);
    color: var(--paper-white);
    display: flex;
    flex-direction: column;
    align-items: center;
    padding-top: 46px;
  }
  .site-name {
    font-size: 38px;
    font-weight: 700;
    letter-spacing: 0.5px;
    line-height: 1;
  }
  .hours-pill {
    margin-top: 10px;
    background: var(--ink-black);
    border-radius: 28px;
    padding: 9px 30px;
    text-align: center;
    font-size: 15px;
    line-height: 1.3;
    font-weight: 400;
  }
  .contact-icon {
    margin-top: 12px;
    width: 22px;
    height: 22px;
    border-radius: 50%;
    background: var(--paper-white);
    display: flex;
    align-items: center;
    justify-content: center;
  }
  .contact-icon svg { width: 13px; height: 13px; }
  .contact-text {
    margin-top: 6px;
    font-size: 16px;
    text-align: center;
    line-height: 1.3;
    letter-spacing: 0.3px;
  }
  .card-back {
    background: var(--card-white);
    display: flex;
    flex-direction: column;
    align-items: center;
    justify-content: center;
  }
  .mascot-art {
    width: 196px;
    height: 100px;
    border-radius: 8px;
    background: linear-gradient(90deg, #ff3b3b 0%, #fb0000 50%, #ff3b3b 100%);
    opacity: 0.85;
  }
  .brand-name {
    margin-top: 10px;
    font-size: 40px;
    font-weight: 900;
    color: var(--ink-black);
    letter-spacing: 1px;
    line-height: 1;
  }
</style>
</head>
<body>
<main class="canvas">
  <section class="card card-front">
    <h1 class="site-name">Zorlivo.com</h1>
    <div class="hours-pill">
      <p>Hours Monday - Friday 10AM - 4PM</p>
      <p>Sat and Sunday Closed</p>
    </div>
    <div class="contact-icon" aria-hidden="true">
      <svg viewBox="0 0 24 24"><path fill="none" stroke="#fb0000" stroke-width="2.2" stroke-linejoin="round" d="M5 3h4l2 5-2.5 1.5a11 11 0 0 0 6 6L16 13l5 2v4a2 2 0 0 1-2 2A16 16 0 0 1 3 5a2 2 0 0 1 2-2z"/></svg>
    </div>
    <p class="contact-text">90 94 718 263</p>
    <div class="contact-icon" aria-hidden="true">
      <svg viewBox="0 0 24 24"><path fill="none" stroke="#fb0000" stroke-width="2.2" d="M12 22s-7-7-7-12a7 7 0 0 1 14 0c0 5-7 12-7 12z"/><circle cx="12" cy="10" r="2.6" fill="none" stroke="#fb0000" stroke-width="2.2"/></svg>
    </div>
    <p class="contact-text">Address is 437 Dunmore Lane Suite<br>C San Bernardino CA 92408</p>
  </section>
  <section class="card card-back">
    <div class="mascot-art" role="img" aria-label="Illustration of two red cartoon characters joined by an arrow, a sad one holding a broken phone and a happy one holding a fixed phone"></div>
    <p class="brand-name">Zorlivo</p>
  </section>
</main>
</body>
</html>
```